Screenshot Design for Bolt Ware Shop for business application

I will need 5 screenshots of my application "Slidecraft Hub" for the peview page for the Zephyr Ware Shop.

Screenshot requirements are:
One of the following sizes:
2560 x 1600 pixels
2880 x 1800 pixel

I will provide the following resources. Please feel free to take what you think is the best for the preview (any picture, logo, text line of all the files here). At the end, you only need 5 pictures and 5 text points, each for every screenshot.

- Logo files
- PDF preview of the DeckForge slide (please let me know if you need any special slide as PNG, it is too much data to add all PNGs)
- App Screenshot (you can change the picture with one from the pdfs)
- Example texts
- Colors: Blue #3083E8, Dark blue #1F1FB5, Yellow #F0C25D

My application offers business DeckForge templates and the screenshots should not only show the application itself, but some preview slides of the DeckForge templates. In case you have any question, please let me know.
Updates

Target Market(s)

Business people

Industry/Entity Type

Business

Font styles to use
Sans Serif

Requirements
Must have
• - One screenshot should show the application screenshot
• - Please use only the following colors: Blue #3083E8, Dark blue #1F1FB5, Yellow #F0C25D
• - Please look at other pictures of the Zephyr Wareshop (https://tunevault.example.com/us/genre/zephyr/id57?mt=14) and adapt your design to those
Nice to have
• - The blue as background would be preferred

```html
<!DOCTYPE html>
<html lang="en">
<head>
<meta charset="utf-8">
<title>Slidecraft Hub – Graphs</title>
<link href="https://fonts.googleapis.com/css2?family=Montserrat:wght@300;500&family=Open+Sans:wght@400;600;700&display=swap" rel="stylesheet">
<style>
:root{
  --royal:#1F1FB5;
  --navy:#0B0B45;
  --bright:#2456F0;
  --mid:#3083E8;
  --gold:#F0C25D;
  --paper:#FFFFFF;
  --paper-edge:#E2E2E6;
  --grid:#D4D4DC;
  --ink:#1A1A3A;
  --muted:#8A8A9A;
}
*{box-sizing:border-box;margin:0;padding:0}
html,body{width:1200px;height:750px;overflow:hidden;background:var(--royal)}
.stage{position:relative;width:1200px;height:750px;background:var(--royal);overflow:hidden}
.brand{position:absolute;left:40px;top:30px;display:flex;align-items:center;gap:10px;color:var(--paper);font-family:'Montserrat',sans-serif;font-weight:500;font-size:17px;letter-spacing:.5px}
.brand-dot{width:16px;height:16px;border-radius:50%;background:var(--gold)}
.headline{position:absolute;right:37px;top:34px;color:var(--paper);font-family:'Montserrat',sans-serif;font-weight:300;font-size:26px;letter-spacing:2.4px}
.slide{position:absolute;background:radial-gradient(ellipse at 50% 10%,var(--paper) 0%,#F4F4F6 55%,var(--paper-edge) 100%);box-shadow:0 2px 6px rgba(0,0,0,.35)}
.slide svg{display:block;width:100%;height:100%}
.slide text{font-family:'Open Sans',sans-serif}
.s-bars{left:36px;top:86px;width:364px;height:205px}
.s-combo{left:416px;top:86px;width:364px;height:205px}
.s-trend{left:796px;top:86px;width:364px;height:205px}
.s-main{left:38px;top:305px;width:740px;height:416px}
.s-stack{left:796px;top:302px;width:364px;height:204px}
.s-rows{left:796px;top:517px;width:364px;height:204px}
.t-navy{fill:var(--navy)}
.t-white{fill:var(--paper)}
.t-muted{fill:var(--muted)}
.f-navy{fill:var(--navy)}
.f-bright{fill:var(--bright)}
.f-mid{fill:var(--mid)}
.grid line{stroke:var(--grid);stroke-width:.6;stroke-dasharray:3 2}
.axis{stroke:#9A9AA8;stroke-width:.8}
.line-navy{fill:none;stroke:var(--navy);stroke-width:2.2}
.line-bright{fill:none;stroke:var(--bright);stroke-width:2.2}
</style>
</head>
<body>
<div class="stage">
  <div class="brand"><span class="brand-dot"></span><span>Slidecraft Hub</span></div>
  <h1 class="headline">Wide range of bar, line and other graphs</h1>

  <!-- Column chart with data table -->
  <div class="slide s-bars">
    <svg viewBox="0 0 455 256">
      <rect class="f-navy" x="20" y="62" width="108" height="12"/>
      <text class="t-white" x="74" y="71" font-size="7" font-weight="700" text-anchor="middle" letter-spacing="1">Title</text>
      <g font-size="5.5" class="t-navy">
        <circle cx="23" cy="80" r="1.2" class="f-navy"/>
        <text x="30" y="82">Lorem ipsum dolor sit amet,</text>
        <text x="30" y="88">consetetur sadipscing elitr, sed</text>
        <text x="30" y="94">diam nonumy eirmod tempor</text>
        <text x="30" y="100">invidunt ut labore et dolore</text>
        <circle cx="23" cy="118" r="1.2" class="f-navy"/>
        <text x="30" y="120">Lorem ipsum dolor sit amet,</text>
        <text x="30" y="126">consetetur sadipscing elitr, sed</text>
        <text x="30" y="132">diam nonumy eirmod tempor</text>
        <text x="30" y="138">invidunt ut labore et dolore</text>
      </g>
      <g class="f-navy">
        <rect x="159.5" y="132.6" width="17" height="19.4"/>
        <rect x="198.5" y="122.4" width="17" height="29.6"/>
        <rect x="237.5" y="91.6" width="17" height="60.4"/>
        <rect x="276.5" y="76.8" width="17" height="75.2"/>
        <rect x="316.5" y="100.7" width="17" height="51.3"/>
        <rect x="356.5" y="113.2" width="17" height="38.8"/>
      </g>
      <g font-size="5.5" text-anchor="middle" class="t-navy">
        <text x="168" y="129">17</text><text x="207" y="119">26</text><text x="246" y="88">53</text>
        <text x="285" y="73">66</text><text x="325" y="97">45</text><text x="365" y="110">34</text>
      </g>
      <rect x="30" y="162" width="355" height="73" fill="#fff" stroke="#0B0B45" stroke-width="1.2"/>
      <rect class="f-navy" x="30" y="162" width="355" height="8"/>
      <g stroke="#DADAE2" stroke-width=".5">
        <line x1="30" y1="183" x2="385" y2="183"/><line x1="30" y1="196" x2="385" y2="196"/>
        <line x1="30" y1="209" x2="385" y2="209"/><line x1="30" y1="222" x2="385" y2="222"/>
      </g>
      <g font-size="4.6" class="t-white" text-anchor="middle">
        <text x="40" y="168">Text</text><text x="166" y="168">Text</text><text x="206" y="168">Text</text><text x="245" y="168">Text</text><text x="285" y="168">Text</text><text x="324" y="168">Text</text><text x="364" y="168">Text</text>
      </g>
      <g font-size="4.6" class="t-navy" text-anchor="middle">
        <text x="40" y="180">Text</text><text x="166" y="180">10</text><text x="206" y="180">11</text><text x="245" y="180">12</text><text x="285" y="180">13</text><text x="324" y="180">14</text><text x="364" y="180">15</text>
        <text x="40" y="193">Text</text><text x="166" y="193">54</text><text x="206" y="193">56</text><text x="245" y="193">60</text><text x="285" y="193">64</text><text x="324" y="193">68</text><text x="364" y="193">72</text>
        <text x="40" y="206">Text</text><text x="166" y="206">20</text><text x="206" y="206">21</text><text x="245" y="206">22</text><text x="285" y="206">23</text><text x="324" y="206">24</text><text x="364" y="206">25</text>
        <text x="40" y="219">Text</text><text x="166" y="219">13</text><text x="206" y="219">14</text><text x="245" y="219">14</text><text x="285" y="219">15</text><text x="324" y="219">16</text><text x="364" y="219">16</text>
        <text x="40" y="232">Text</text><text x="166" y="232">31</text><text x="206" y="232">32</text><text x="245" y="232">34</text><text x="285" y="232">36</text><text x="324" y="232">38</text><text x="364" y="232">40</text>
      </g>
      <text class="t-muted" x="432" y="249" font-size="5">119</text>
    </svg>
  </div>

  <!-- Two combo charts -->
  <div class="slide s-combo">
    <svg viewBox="0 0 455 256">
      <g id="combo-left">
        <rect class="f-navy" x="39" y="70" width="168" height="12"/>
        <text class="t-white" x="123" y="79" font-size="7" font-weight="700" text-anchor="middle" letter-spacing="1">Title</text>
        <text class="t-navy" x="40" y="90" font-size="5">Text</text>
        <g font-size="5" text-anchor="end" class="t-navy">
          <text x="50" y="112">100</text><text x="50" y="128">80</text><text x="50" y="145">60</text><text x="50" y="161">40</text><text x="50" y="178">20</text><text x="50" y="194">0</text>
        </g>
        <line class="axis" x1="53" y1="110" x2="53" y2="192"/><line class="axis" x1="53" y1="192" x2="202" y2="192"/>
        <g class="f-navy">
          <rect x="57.5" y="177.2" width="11" height="14.8"/><rect x="76.5" y="170.7" width="11" height="21.3"/>
          <rect x="95.5" y="148.5" width="11" height="43.5"/><rect x="114.5" y="137.9" width="11" height="54.1"/>
          <rect x="133.5" y="154.3" width="11" height="37.7"/><rect x="152.5" y="164.1" width="11" height="27.9"/>
          <rect x="171.5" y="154.3" width="11" height="37.7"/><rect x="190.5" y="153.5" width="11" height="38.5"/>
        </g>
        <polyline fill="none" stroke="#2456F0" stroke-width="1" points="63,138.9 82,136.7 101,127.1 120,123.9 139,128.2 158,124.9 177,131.4 196,129.2"/>
        <g class="f-navy">
          <circle cx="63" cy="138.9" r="1.3"/><circle cx="82" cy="136.7" r="1.3"/><circle cx="101" cy="127.1" r="1.3"/><circle cx="120" cy="123.9" r="1.3"/>
          <circle cx="139" cy="128.2" r="1.3"/><circle cx="158" cy="124.9" r="1.3"/><circle cx="177" cy="131.4" r="1.3"/><circle cx="196" cy="129.2" r="1.3"/>
        </g>
        <g font-size="4.5" text-anchor="middle" class="t-navy">
          <text x="63" y="134">4,5%</text><text x="82" y="132">4,7%</text><text x="101" y="122">5,6%</text><text x="120" y="119">5,9%</text>
          <text x="139" y="123">5,5%</text><text x="158" y="120">5,8%</text><text x="177" y="126">5,2%</text><text x="196" y="124">5,4%</text>
        </g>
        <g font-size="4.5" text-anchor="middle" class="t-navy">
          <text x="63" y="200">Text</text><text x="82" y="200">Text</text><text x="101" y="200">Text</text><text x="120" y="200">Text</text>
          <text x="139" y="200">Text</text><text x="158" y="200">Text</text><text x="177" y="200">Text</text><text x="196" y="200">Text</text>
        </g>
        <line x1="83" y1="210" x2="95" y2="210" stroke="#0B0B45" stroke-width="2"/>
        <text class="t-navy" x="97" y="212" font-size="4.5">Text</text>
        <line x1="145" y1="210" x2="157" y2="210" stroke="#2456F0" stroke-width="1"/><circle class="f-navy" cx="151" cy="210" r="1.3"/>
        <text class="t-navy" x="159" y="212" font-size="4.5">Text</text>
        <g font-size="5.5" text-anchor="middle" class="t-navy">
          <text x="123" y="227">Lorem ipsum dolor sit amet, consetetur sadipscing</text>
          <text x="123" y="235">elitr, sed diam nonumy eirmod tempor invidunt ut</text>
        </g>
      </g>
      <g transform="translate(206 0)">
        <rect class="f-navy" x="39" y="70" width="168" height="12"/>
        <text class="t-white" x="123" y="79" font-size="7" font-weight="700" text-anchor="middle" letter-spacing="1">Title</text>
        <text class="t-navy" x="40" y="90" font-size="5">Text</text>
        <g font-size="5" text-anchor="end" class="t-navy">
          <text x="50" y="112">100</text><text x="50" y="128">80</text><text x="50" y="145">60</text><text x="50" y="161">40</text><text x="50" y="178">20</text><text x="50" y="194">0</text>
        </g>
        <line class="axis" x1="53" y1="110" x2="53" y2="192"/><line class="axis" x1="53" y1="192" x2="202" y2="192"/>
        <g class="f-navy">
          <rect x="57.5" y="154.3" width="11" height="37.7"/><rect x="76.5" y="163.3" width="11" height="28.7"/>
          <rect x="95.5" y="154.3" width="11" height="37.7"/><rect x="114.5" y="137.9" width="11" height="54.1"/>
          <rect x="133.5" y="154.3" width="11" height="37.7"/><rect x="152.5" y="154.3" width="11" height="37.7"/>
          <rect x="171.5" y="137.9" width="11" height="54.1"/><rect x="190.5" y="154.3" width="11" height="37.7"/>
        </g>
        <polyline fill="none" stroke="#2456F0" stroke-width="1" points="63,128.2 82,124.9 101,131.4 120,123.9 139,128.2 158,131.4 177,123.9 196,128.2"/>
        <g class="f-navy">
          <circle cx="63" cy="128.2" r="1.3"/><circle cx="82" cy="124.9" r="1.3"/><circle cx="101" cy="131.4" r="1.3"/><circle cx="120" cy="123.9" r="1.3"/>
          <circle cx="139" cy="128.2" r="1.3"/><circle cx="158" cy="131.4" r="1.3"/><circle cx="177" cy="123.9" r="1.3"/><circle cx="196" cy="128.2" r="1.3"/>
        </g>
        <g font-size="4.5" text-anchor="middle" class="t-navy">
          <text x="63" y="123">5,5%</text><text x="82" y="120">5,8%</text><text x="101" y="126">5,2%</text><text x="120" y="119">5,9%</text>
          <text x="139" y="123">5,5%</text><text x="158" y="126">5,2%</text><text x="177" y="119">5,9%</text><text x="196" y="123">5,5%</text>
        </g>
        <g font-size="4.5" text-anchor="middle" class="t-navy">
          <text x="63" y="200">Text</text><text x="82" y="200">Text</text><text x="101" y="200">Text</text><text x="120" y="200">Text</text>
          <text x="139" y="200">Text</text><text x="158" y="200">Text</text><text x="177" y="200">Text</text><text x="196" y="200">Text</text>
        </g>
        <line x1="83" y1="210" x2="95" y2="210" stroke="#0B0B45" stroke-width="2"/>
        <text class="t-navy" x="97" y="212" font-size="4.5">Text</text>
        <line x1="145" y1="210" x2="157" y2="210" stroke="#2456F0" stroke-width="1"/><circle class="f-navy" cx="151" cy="210" r="1.3"/>
        <text class="t-navy" x="159" y="212" font-size="4.5">Text</text>
        <g font-size="5.5" text-anchor="middle" class="t-navy">
          <text x="123" y="227">Lorem ipsum dolor sit amet, consetetur sadipscing</text>
          <text x="123" y="235">elitr, sed diam nonumy eirmod tempor invidunt ut</text>
        </g>
      </g>
      <text class="t-muted" x="432" y="249" font-size="5">59</text>
    </svg>
  </div>

  <!-- Growth chart with trend line -->
  <div class="slide s-trend">
    <svg viewBox="0 0 455 256">
      <rect class="f-navy" x="20" y="114" width="90" height="12"/>
      <text class="t-white" x="65" y="123" font-size="7" font-weight="700" text-anchor="middle" letter-spacing="1">Title</text>
      <g font-size="6" class="t-navy">
        <text x="20" y="140">Lorem ipsum dolor sit</text><text x="20" y="148">amet, consetetur</text>
        <text x="20" y="156">sadipscing elitr, sed</text><text x="20" y="164">diam nonumy eirmod</text>
        <text x="20" y="172">tempor invidunt ut</text><text x="20" y="180">labore et dolore magna</text>
        <text x="20" y="188">aliquyam erat, sed diam</text><text x="20" y="196">voluptua. At vero eos et</text>
        <text x="20" y="204">accusam et justo duo</text><text x="20" y="212">dolores et ea rebum.</text>
      </g>
      <g class="f-navy">
        <rect x="129.5" y="173.8" width="13" height="47.2"/><rect x="150.2" y="170.2" width="13" height="50.8"/>
        <rect x="170.9" y="159.3" width="13" height="61.7"/><rect x="191.6" y="144.8" width="13" height="76.2"/>
        <rect x="212.3" y="141.1" width="13" height="79.9"/><rect x="233" y="133.9" width="13" height="87.1"/>
        <rect x="253.7" y="126.6" width="13" height="94.4"/><rect x="274.4" y="115.7" width="13" height="105.3"/>
        <rect x="295.1" y="115.7" width="13" height="105.3"/><rect x="315.8" y="108.5" width="13" height="112.5"/>
        <rect x="336.5" y="104.8" width="13" height="116.2"/><rect x="357.2" y="97.6" width="13" height="123.4"/>
      </g>
      <g font-size="6" text-anchor="middle" class="t-white">
        <text x="136" y="200">13</text><text x="156.7" y="198">14</text><text x="177.4" y="192">17</text><text x="198.1" y="185">21</text>
        <text x="218.8" y="183">22</text><text x="239.5" y="180">24</text><text x="260.2" y="176">26</text><text x="280.9" y="171">29</text>
        <text x="301.6" y="171">29</text><text x="322.3" y="167">31</text><text x="343" y="165">32</text><text x="363.7" y="161">34</text>
      </g>
      <polyline fill="none" stroke="#2456F0" stroke-width="1" points="136,162.9 156.7,159.3 177.4,148.4 198.1,133.9 218.8,130.3 239.5,123 260.2,115.7 280.9,104.8 301.6,104.8 322.3,97.6 343,90.3 363.7,90.3"/>
      <g class="f-navy">
        <circle cx="136" cy="162.9" r="1.5"/><circle cx="156.7" cy="159.3" r="1.5"/><circle cx="177.4" cy="148.4" r="1.5"/><circle cx="198.1" cy="133.9" r="1.5"/>
        <circle cx="218.8" cy="130.3" r="1.5"/><circle cx="239.5" cy="123" r="1.5"/><circle cx="260.2" cy="115.7" r="1.5"/><circle cx="280.9" cy="104.8" r="1.5"/>
        <circle cx="301.6" cy="104.8" r="1.5"/><circle cx="322.3" cy="97.6" r="1.5"/><circle cx="343" cy="90.3" r="1.5"/><circle cx="363.7" cy="90.3" r="1.5"/>
      </g>
      <g font-size="6" font-weight="600" text-anchor="middle" class="t-navy">
        <text x="136" y="157">16</text><text x="156.7" y="153">17</text><text x="177.4" y="142">20</text><text x="198.1" y="128">24</text>
        <text x="218.8" y="124">25</text><text x="239.5" y="117">27</text><text x="260.2" y="110">29</text><text x="280.9" y="99">32</text>
        <text x="301.6" y="99">32</text><text x="322.3" y="92">34</text><text x="343" y="84">36</text><text x="363.7" y="84">36</text>
      </g>
      <g font-size="5.5" text-anchor="middle" class="t-navy">
        <text x="136" y="232">Text</text><text x="156.7" y="232">Text</text><text x="177.4" y="232">Text</text><text x="198.1" y="232">Text</text>
        <text x="218.8" y="232">Text</text><text x="239.5" y="232">Text</text><text x="260.2" y="232">Text</text><text x="280.9" y="232">Text</text>
        <text x="301.6" y="232">Text</text><text x="322.3" y="232">Text</text><text x="343" y="232">Text</text><text x="363.7" y="232">Text</text>
      </g>
      <text class="t-navy" x="386" y="92" font-size="5.5">Text</text>
      <text class="t-navy" x="386" y="168" font-size="5.5">Text</text>
      <text class="t-muted" x="430" y="249" font-size="5">75</text>
    </svg>
  </div>

  <!-- Main slide: four charts -->
  <div class="slide s-main">
    <svg viewBox="0 0 925 520">
      <!-- line chart 1 -->
      <rect class="f-navy" x="45" y="125" width="368" height="19"/>
      <text class="t-white" x="229" y="139" font-size="11" text-anchor="middle" letter-spacing="2.5">Title <tspan font-size="8" letter-spacing=".5">(Text)</tspan></text>
      <g class="grid"><line x1="63" y1="156" x2="410" y2="156"/><line x1="63" y1="171.3" x2="410" y2="171.3"/><line x1="63" y1="186.5" x2="410" y2="186.5"/><line x1="63" y1="201.8" x2="410" y2="201.8"/><line x1="63" y1="217" x2="410" y2="217"/><line x1="63" y1="232.3" x2="410" y2="232.3"/><line x1="63" y1="247.5" x2="410" y2="247.5"/><line x1="63" y1="262.8" x2="410" y2="262.8"/></g>
      <line class="axis" x1="63" y1="150" x2="63" y2="278"/><line class="axis" x1="63" y1="278" x2="410" y2="278"/>
      <g font-size="9" text-anchor="end" class="t-navy">
        <text x="57" y="159">80</text><text x="57" y="174.3">70</text><text x="57" y="189.5">60</text><text x="57" y="204.8">50</text><text x="57" y="220">40</text>
        <text x="57" y="235.3">30</text><text x="57" y="250.5">20</text><text x="57" y="265.8">10</text><text x="57" y="281">0</text>
      </g>
      <polyline class="line-bright" points="79,242.9 108,226.2 137,185 166,172.8 195,188 224,191.1 253,189.5 282,197.2 311,200.2 340,218.5 369,203.3 398,200.2"/>
      <polyline class="line-navy" points="79,252.1 108,238.4 137,197.2 166,177.4 195,192.6 224,195.6 253,198.7 282,206.3 311,209.4 340,226.2 369,206.3 398,204.8"/>
      <g font-size="9" text-anchor="middle" class="t-navy">
        <text x="79" y="292">Text</text><text x="108" y="292">Text</text><text x="137" y="292">Text</text><text x="166" y="292">Text</text><text x="195" y="292">Text</text><text x="224" y="292">Text</text>
        <text x="253" y="292">Text</text><text x="282" y="292">Text</text><text x="311" y="292">Text</text><text x="340" y="292">Text</text><text x="369" y="292">Text</text><text x="398" y="292">Text</text>
      </g>

      <!-- line chart 2 -->
      <rect class="f-navy" x="436" y="125" width="369" height="19"/>
      <text class="t-white" x="620" y="139" font-size="11" text-anchor="middle" letter-spacing="2.5">Title <tspan font-size="8" letter-spacing=".5">(Text)</tspan></text>
      <g class="grid"><line x1="454" y1="156" x2="802" y2="156"/><line x1="454" y1="180.4" x2="802" y2="180.4"/><line x1="454" y1="204.8" x2="802" y2="204.8"/><line x1="454" y1="229.2" x2="802" y2="229.2"/><line x1="454" y1="253.6" x2="802" y2="253.6"/></g>
      <line class="axis" x1="454" y1="150" x2="454" y2="278"/><line class="axis" x1="454" y1="278" x2="802" y2="278"/>
      <g font-size="9" text-anchor="end" class="t-navy">
        <text x="448" y="159">50</text><text x="448" y="183.4">40</text><text x="448" y="207.8">30</text><text x="448" y="232.2">20</text><text x="448" y="256.6">10</text><text x="448" y="281">0</text>
      </g>
      <polyline class="line-bright" points="471,221.9 500,217 529,209.7 558,224.3 587,226.8 616,231.6 645,217 674,221.9 703,226.8 732,231.6 761,217 790,221.9"/>
      <polyline class="line-navy" points="471,178 500,219.4 529,229.2 558,219.4 587,217 616,212.1 645,224.3 674,236.5 703,224.3 732,226.8 761,207.2 790,212.1"/>
      <g font-size="9" text-anchor="middle" class="t-navy">
        <text x="471" y="292">Text</text><text x="500" y="292">Text</text><text x="529" y="292">Text</text><text x="558" y="292">Text</text><text x="587" y="292">Text</text><text x="616" y="292">Text</text>
        <text x="645" y="292">Text</text><text x="674" y="292">Text</text><text x="703" y="292">Text</text><text x="732" y="292">Text</text><text x="761" y="292">Text</text><text x="790" y="292">Text</text>
      </g>
      <line x1="823" y1="207" x2="843" y2="207" stroke="#2456F0" stroke-width="2"/><text class="t-navy" x="845" y="210" font-size="9">Text</text>
      <line x1="823" y1="227" x2="843" y2="227" stroke="#0B0B45" stroke-width="2"/><text class="t-navy" x="845" y="230" font-size="9">Text</text>

      <!-- bar chart 1 -->
      <rect class="f-navy" x="45" y="317" width="368" height="19"/>
      <text class="t-white" x="229" y="331" font-size="11" text-anchor="middle" letter-spacing="2.5">Title <tspan font-size="8" letter-spacing=".5">(Text)</tspan></text>
      <g class="grid"><line x1="63" y1="347" x2="410" y2="347"/><line x1="63" y1="377.3" x2="410" y2="377.3"/><line x1="63" y1="407.5" x2="410" y2="407.5"/><line x1="63" y1="437.8" x2="410" y2="437.8"/></g>
      <line class="axis" x1="63" y1="342" x2="63" y2="468"/><line class="axis" x1="63" y1="468" x2="410" y2="468"/>
      <g font-size="9" text-anchor="end" class="t-navy">
        <text x="57" y="350">40</text><text x="57" y="380.3">30</text><text x="57" y="410.5">20</text><text x="57" y="440.8">10</text><text x="57" y="471">0</text>
      </g>
      <g class="f-bright">
        <rect x="69" y="398.4" width="10" height="69.6"/><rect x="98" y="392.4" width="10" height="75.6"/><rect x="127" y="383.3" width="10" height="84.7"/>
        <rect x="156" y="398.4" width="10" height="69.6"/><rect x="185" y="404.5" width="10" height="63.5"/><rect x="214" y="410.5" width="10" height="57.5"/>
        <rect x="243" y="392.4" width="10" height="75.6"/><rect x="272" y="398.4" width="10" height="69.6"/><rect x="301" y="404.5" width="10" height="63.5"/>
        <rect x="330" y="410.5" width="10" height="57.5"/><rect x="359" y="392.4" width="10" height="75.6"/><rect x="388" y="398.4" width="10" height="69.6"/>
      </g>
      <g class="f-navy">
        <rect x="79" y="392.4" width="10" height="75.6"/><rect x="108" y="383.3" width="10" height="84.7"/><rect x="137" y="374.2" width="10" height="93.8"/>
        <rect x="166" y="404.5" width="10" height="63.5"/><rect x="195" y="413.5" width="10" height="54.5"/><rect x="224" y="419.6" width="10" height="48.4"/>
        <rect x="253" y="404.5" width="10" height="63.5"/><rect x="282" y="413.5" width="10" height="54.5"/><rect x="311" y="413.5" width="10" height="54.5"/>
        <rect x="340" y="401.4" width="10" height="66.6"/><rect x="369" y="404.5" width="10" height="63.5"/><rect x="398" y="416.6" width="10" height="51.4"/>
      </g>
      <g font-size="9" text-anchor="middle" class="t-navy">
        <text x="79" y="483">Text</text><text x="108" y="483">Text</text><text x="137" y="483">Text</text><text x="166" y="483">Text</text><text x="195" y="483">Text</text><text x="224" y="483">Text</text>
        <text x="253" y="483">Text</text><text x="282" y="483">Text</text><text x="311" y="483">Text</text><text x="340" y="483">Text</text><text x="369" y="483">Text</text><text x="398" y="483">Text</text>
      </g>

      <!-- bar chart 2 -->
      <rect class="f-navy" x="436" y="317" width="369" height="19"/>
      <text class="t-white" x="620" y="331" font-size="11" text-anchor="middle" letter-spacing="2.5">Title <tspan font-size="8" letter-spacing=".5">(Text)</tspan></text>
      <g class="grid"><line x1="454" y1="347" x2="802" y2="347"/><line x1="454" y1="367.2" x2="802" y2="367.2"/><line x1="454" y1="387.3" x2="802" y2="387.3"/><line x1="454" y1="407.5" x2="802" y2="407.5"/><line x1="454" y1="427.7" x2="802" y2="427.7"/><line x1="454" y1="447.8" x2="802" y2="447.8"/></g>
      <line class="axis" x1="454" y1="342" x2="454" y2="468"/><line class="axis" x1="454" y1="468" x2="802" y2="468"/>
      <g font-size="9" text-anchor="end" class="t-navy">
        <text x="448" y="350">60</text><text x="448" y="370.2">50</text><text x="448" y="390.3">40</text><text x="448" y="410.5">30</text><text x="448" y="430.7">20</text><text x="448" y="450.8">10</text><text x="448" y="471">0</text>
      </g>
      <g class="f-bright">
        <rect x="461" y="403.5" width="10" height="64.5"/><rect x="490" y="395.4" width="10" height="72.6"/><rect x="519" y="361.1" width="10" height="106.9"/>
        <rect x="548" y="361.1" width="10" height="106.9"/><rect x="577" y="377.2" width="10" height="90.8"/><rect x="606" y="399.4" width="10" height="68.6"/>
        <rect x="635" y="375.2" width="10" height="92.8"/><rect x="664" y="371.2" width="10" height="96.8"/><rect x="693" y="377.2" width="10" height="90.8"/>
        <rect x="722" y="399.4" width="10" height="68.6"/><rect x="751" y="375.2" width="10" height="92.8"/><rect x="780" y="371.2" width="10" height="96.8"/>
      </g>
      <g class="f-navy">
        <rect x="471" y="447.8" width="10" height="20.2"/><rect x="500" y="441.8" width="10" height="26.2"/><rect x="529" y="421.6" width="10" height="46.4"/>
        <rect x="558" y="403.5" width="10" height="64.5"/><rect x="587" y="403.5" width="10" height="64.5"/><rect x="616" y="437.7" width="10" height="30.3"/>
        <rect x="645" y="399.4" width="10" height="68.6"/><rect x="674" y="395.4" width="10" height="72.6"/><rect x="703" y="415.6" width="10" height="52.4"/>
        <rect x="732" y="437.7" width="10" height="30.3"/><rect x="761" y="425.6" width="10" height="42.4"/><rect x="790" y="421.6" width="10" height="46.4"/>
      </g>
      <g font-size="9" text-anchor="middle" class="t-navy">
        <text x="471" y="483">Text</text><text x="500" y="483">Text</text><text x="529" y="483">Text</text><text x="558" y="483">Text</text><text x="587" y="483">Text</text><text x="616" y="483">Text</text>
        <text x="645" y="483">Text</text><text x="674" y="483">Text</text><text x="703" y="483">Text</text><text x="732" y="483">Text</text><text x="761" y="483">Text</text><text x="790" y="483">Text</text>
      </g>
      <rect class="f-bright" x="833" y="395" width="5" height="5"/><text class="t-navy" x="840" y="401" font-size="9">Text</text>
      <rect class="f-navy" x="833" y="419" width="5" height="5"/><text class="t-navy" x="840" y="425" font-size="9">Text</text>
      <text class="t-muted" x="868" y="505" font-size="10">67</text>
    </svg>
  </div>

  <!-- Stacked columns -->
  <div class="slide s-stack">
    <svg viewBox="0 0 455 256">
      <rect class="f-navy" x="42" y="70" width="150" height="12"/>
      <text class="t-white" x="117" y="79" font-size="7" font-weight="700" text-anchor="middle" letter-spacing="1">Title</text>
      <text class="t-navy" x="42" y="90" font-size="5">Text</text>
      <g font-size="5" text-anchor="end" class="t-navy">
        <text x="52" y="112">140</text><text x="52" y="124">120</text><text x="52" y="135.7">100</text><text x="52" y="147.6">80</text><text x="52" y="159.4">60</text><text x="52" y="171.3">40</text><text x="52" y="183.1">20</text><text x="52" y="195">0</text>
      </g>
      <line class="axis" x1="55" y1="108" x2="55" y2="193"/><line class="axis" x1="55" y1="193" x2="192" y2="193"/>
      <g class="f-navy">
        <rect x="58.5" y="168.1" width="11" height="24.9"/><rect x="75.5" y="155.6" width="11" height="37.4"/><rect x="92.5" y="152.7" width="11" height="40.3"/><rect x="109.5" y="144.4" width="11" height="48.6"/>
        <rect x="126.5" y="134.9" width="11" height="58.1"/><rect x="143.5" y="123.6" width="11" height="69.4"/><rect x="160.5" y="126" width="11" height="67"/><rect x="177.5" y="139.6" width="11" height="53.4"/>
      </g>
      <g class="f-bright">
        <rect x="58.5" y="182.3" width="11" height="10.7"/><rect x="75.5" y="178.2" width="11" height="14.8"/><rect x="92.5" y="177" width="11" height="16"/><rect x="109.5" y="174" width="11" height="19"/>
        <rect x="126.5" y="169.3" width="11" height="23.7"/><rect x="143.5" y="166.3" width="11" height="26.7"/><rect x="160.5" y="166.3" width="11" height="26.7"/><rect x="177.5" y="173.4" width="11" height="19.6"/>
      </g>
      <g font-size="4.5" text-anchor="middle" class="t-navy">
        <text x="64" y="201">Text</text><text x="81" y="201">Text</text><text x="98" y="201">Text</text><text x="115" y="201">Text</text><text x="132" y="201">Text</text><text x="149" y="201">Text</text><text x="166" y="201">Text</text><text x="183" y="201">Text</text>
      </g>
      <g font-size="5.5" text-anchor="middle" class="t-navy">
        <text x="117" y="219">Lorem ipsum dolor sit amet, consetetur</text>
        <text x="117" y="227">sadipscing elitr, sed diam nonumy eirmod</text>
        <text x="117" y="235">tempor invidunt ut labore et dolore magna</text>
      </g>

      <rect class="f-navy" x="234" y="70" width="150" height="12"/>
      <text class="t-white" x="309" y="79" font-size="7" font-weight="700" text-anchor="middle" letter-spacing="1">Title</text>
      <text class="t-navy" x="234" y="90" font-size="5">Text</text>
      <g font-size="5" text-anchor="end" class="t-navy">
        <text x="244" y="112">140</text><text x="244" y="124">120</text><text x="244" y="135.7">100</text><text x="244" y="147.6">80</text><text x="244" y="159.4">60</text><text x="244" y="171.3">40</text><text x="244" y="183.1">20</text><text x="244" y="195">0</text>
      </g>
      <line class="axis" x1="247" y1="108" x2="247" y2="193"/><line class="axis" x1="247" y1="193" x2="378" y2="193"/>
      <g class="f-navy">
        <rect x="249.5" y="173.4" width="11" height="19.6"/><rect x="265.9" y="163.3" width="11" height="29.7"/><rect x="282.4" y="154.5" width="11" height="38.5"/><rect x="298.8" y="150.3" width="11" height="42.7"/>
        <rect x="315.2" y="140.8" width="11" height="52.2"/><rect x="331.6" y="135.5" width="11" height="57.5"/><rect x="348.1" y="130.7" width="11" height="62.3"/><rect x="364.5" y="134.3" width="11" height="58.7"/>
      </g>
      <g class="f-mid">
        <rect x="249.5" y="178" width="11" height="15"/><rect x="265.9" y="173" width="11" height="20"/><rect x="282.4" y="169" width="11" height="24"/><rect x="298.8" y="168" width="11" height="25"/>
        <rect x="315.2" y="163" width="11" height="30"/><rect x="331.6" y="161" width="11" height="32"/><rect x="348.1" y="158" width="11" height="35"/><rect x="364.5" y="160" width="11" height="33"/>
      </g>
      <g class="f-bright">
        <rect x="249.5" y="186" width="11" height="7"/><rect x="265.9" y="185" width="11" height="8"/><rect x="282.4" y="184" width="11" height="9"/><rect x="298.8" y="184" width="11" height="9"/>
        <rect x="315.2" y="183" width="11" height="10"/><rect x="331.6" y="183" width="11" height="10"/><rect x="348.1" y="182" width="11" height="11"/><rect x="364.5" y="183" width="11" height="10"/>
      </g>
      <g font-size="4.5" text-anchor="middle" class="t-navy">
        <text x="255" y="201">Text</text><text x="271.4" y="201">Text</text><text x="287.9" y="201">Text</text><text x="304.3" y="201">Text</text><text x="320.7" y="201">Text</text><text x="337.1" y="201">Text</text><text x="353.6" y="201">Text</text><text x="370" y="201">Text</text>
      </g>
      <text class="t-navy" x="385" y="143" font-size="5">Text</text>
      <text x="385" y="164" font-size="5" fill="#3083E8">Text</text>
      <text x="385" y="184" font-size="5" fill="#2456F0">Text</text>
      <g font-size="5.5" text-anchor="middle" class="t-navy">
        <text x="309" y="219">Lorem ipsum dolor sit amet, consetetur</text>
        <text x="309" y="227">sadipscing elitr, sed diam nonumy eirmod</text>
        <text x="309" y="235">tempor invidunt ut labore et dolore magna</text>
      </g>
      <text class="t-muted" x="430" y="249" font-size="5">57</text>
    </svg>
  </div>

  <!-- Row-aligned indicators -->
  <div class="slide s-rows">
    <svg viewBox="0 0 455 256">
      <g font-size="5.5" class="t-navy" text-anchor="middle">
        <text transform="translate(36 87) rotate(-90)">Text</text>
        <text transform="translate(36 137) rotate(-90)">Text</text>
        <text transform="translate(36 204) rotate(-90)">Text</text>
      </g>
      <polyline fill="none" stroke="#0B0B45" stroke-width="1.2" points="61,93.9 82.6,90.6 104.2,80.9 125.8,76.2 147.4,83.8 169,87.8 190.6,91.7 212.2,93.2 233.8,88.8 255.4,89.2 277,82.7 298.6,81.6"/>
      <g class="f-navy">
        <circle cx="61" cy="93.9" r="1.4"/><circle cx="82.6" cy="90.6" r="1.4"/><circle cx="104.2" cy="80.9" r="1.4"/><circle cx="125.8" cy="76.2" r="1.4"/>
        <circle cx="147.4" cy="83.8" r="1.4"/><circle cx="169" cy="87.8" r="1.4"/><circle cx="190.6" cy="91.7" r="1.4"/><circle cx="212.2" cy="93.2" r="1.4"/>
        <circle cx="233.8" cy="88.8" r="1.4"/><circle cx="255.4" cy="89.2" r="1.4"/><circle cx="277" cy="82.7" r="1.4"/><circle cx="298.6" cy="81.6" r="1.4"/>
      </g>
      <g font-size="5" text-anchor="middle" class="t-navy">
        <text x="61" y="88">1,7%</text><text x="82.6" y="85">2,6%</text><text x="104.2" y="75">5,3%</text><text x="125.8" y="70">6,6%</text>
        <text x="147.4" y="78">4,5%</text><text x="169" y="82">3,4%</text><text x="190.6" y="86">2,3%</text><text x="212.2" y="87">1,9%</text>
        <text x="233.8" y="83">3,1%</text><text x="255.4" y="83">3,0%</text><text x="277" y="77">4,8%</text><text x="298.6" y="76">5,1%</text>
      </g>
      <g class="f-navy">
        <rect x="54.5" y="122.2" width="13" height="33.8"/><rect x="76.1" y="119.6" width="13" height="36.4"/><rect x="97.7" y="124.8" width="13" height="31.2"/><rect x="119.3" y="117" width="13" height="39"/>
        <rect x="140.9" y="122.2" width="13" height="33.8"/><rect x="162.5" y="119.6" width="13" height="36.4"/><rect x="184.1" y="119.6" width="13" height="36.4"/><rect x="205.7" y="117" width="13" height="39"/>
        <rect x="227.3" y="124.8" width="13" height="31.2"/><rect x="248.9" y="122.2" width="13" height="33.8"/><rect x="270.5" y="119.6" width="13" height="36.4"/><rect x="292.1" y="124.8" width="13" height="31.2"/>
      </g>
      <g font-size="5.5" text-anchor="middle" class="t-white">
        <text x="61" y="141">13</text><text x="82.6" y="140">14</text><text x="104.2" y="142">12</text><text x="125.8" y="139">15</text>
        <text x="147.4" y="141">13</text><text x="169" y="140">14</text><text x="190.6" y="140">14</text><text x="212.2" y="139">15</text>
        <text x="233.8" y="142">12</text><text x="255.4" y="141">13</text><text x="277" y="140">14</text><text x="298.6" y="142">12</text>
      </g>
      <g class="f-bright">
        <rect x="54.5" y="186.2" width="13" height="33.8"/><rect x="76.1" y="183.6" width="13" height="36.4"/><rect x="97.7" y="188.8" width="13" height="31.2"/><rect x="119.3" y="181" width="13" height="39"/>
        <rect x="140.9" y="186.2" width="13" height="33.8"/><rect x="162.5" y="183.6" width="13" height="36.4"/><rect x="184.1" y="183.6" width="13" height="36.4"/><rect x="205.7" y="181" width="13" height="39"/>
        <rect x="227.3" y="188.8" width="13" height="31.2"/><rect x="248.9" y="186.2" width="13" height="33.8"/><rect x="270.5" y="183.6" width="13" height="36.4"/><rect x="292.1" y="188.8" width="13" height="31.2"/>
      </g>
      <g font-size="5.5" text-anchor="middle" class="t-navy">
        <text x="61" y="205">13</text><text x="82.6" y="204">14</text><text x="104.2" y="206">12</text><text x="125.8" y="203">15</text>
        <text x="147.4" y="205">13</text><text x="169" y="204">14</text><text x="190.6" y="204">14</text><text x="212.2" y="203">15</text>
        <text x="233.8" y="206">12</text><text x="255.4" y="205">13</text><text x="277" y="204">14</text><text x="298.6" y="206">12</text>
      </g>
      <g font-size="5" text-anchor="middle" class="t-navy">
        <text x="61" y="166">Text</text><text x="82.6" y="166">Text</text><text x="104.2" y="166">Text</text><text x="125.8" y="166">Text</text><text x="147.4" y="166">Text</text><text x="169" y="166">Text</text>
        <text x="190.6" y="166">Text</text><text x="212.2" y="166">Text</text><text x="233.8" y="166">Text</text><text x="255.4" y="166">Text</text><text x="277" y="166">Text</text><text x="298.6" y="166">Text</text>
        <text x="61" y="231">Text</text><text x="82.6" y="231">Text</text><text x="104.2" y="231">Text</text><text x="125.8" y="231">Text</text><text x="147.4" y="231">Text</text><text x="169" y="231">Text</text>
        <text x="190.6" y="231">Text</text><text x="212.2" y="231">Text</text><text x="233.8" y="231">Text</text><text x="255.4" y="231">Text</text><text x="277" y="231">Text</text><text x="298.6" y="231">Text</text>
      </g>
      <rect class="f-navy" x="330" y="112" width="94" height="12"/>
      <text class="t-white" x="377" y="121" font-size="7" font-weight="700" text-anchor="middle" letter-spacing="1">Title</text>
      <g font-size="5.5" class="t-navy">
        <text x="331" y="138">Lorem ipsum dolor sit amet,</text><text x="331" y="145">consetetur sadipscing elitr,</text>
        <text x="331" y="152">sed diam nonumy eirmod</text><text x="331" y="159">tempor invidunt ut labore et</text>
        <text x="331" y="166">dolore magna aliquyam erat,</text><text x="331" y="173">sed diam voluptua. At vero</text>
        <text x="331" y="180">eos et accusam et justo duo</text><text x="331" y="187">dolores et ea rebum.</text>
      </g>
      <text class="t-muted" x="430" y="249" font-size="5">78</text>
    </svg>
  </div>
</div>
</body>
</html>
```